Blog Banner Design Project: Harbour Lantern Guides

Looking for a new banner for my blog " Owen Pelsworth's Harbour Lantern Guides" at http://www.harbourlanternguides-demo.net - and once design agreed also want an updated album art for the podcast that goes along with the site.
For more about the blog and what it is about:
http://www.harbourlanternguides-demo.net/about
Harbour Lantern Guides is a Luxury Travel Blog And Podcast that provides inspiration, advice and tips about luxurious travel experiences, including destinations, transportation, accommodation, and journeys, that travellers can read, listen to or watch.
Objective of the new design
(1) retain the colour scheme ideally to retain the brand identity, as have been using these colours since 2005.
(2) introduce more of my personality and make it more visually and overt that it is "Owen Pelsworth's Harbour Lantern Guides", so possibly introducing my image into the blog banner so visitors are clear and more aware of the person behind the brand.
(3) needs to have an up-market, luxury but modern feel.
(4) if possible reflect the focus on the content (destinations, transportation, accommodation, attractions and journeys) - but this maybe best left to just words as want the design to be bold and more of the branding and personality.
Ideal wording
Smallish: Owen Pelsworth's
Main wording: Harbour Lantern Guides
Sub-title/ small: luxurious destinations, transportation, accommodation and journeys.
I have a poll running with readers of my blog to rate the designs to help me to chose the final route, and so there is no need to submit any more designs. I will make the decision once the poll closes on the weekend.

```html
<!DOCTYPE html>
<html lang="en">
<head>
<meta charset="utf-8">
<title>Owen Pelsworth's Harbour Lantern Guides – Blog Banner</title>
<link rel="stylesheet" href="https://fonts.googleapis.com/css2?family=Philosopher:wght@400;700&family=Noto+Serif:wght@700&display=swap">
<style>
  :root {
    --sky-top: #c9c2ae;
    --sky-mid: #e6dcc4;
    --sea: #a7aaa3;
    --sand: #b9ab8d;
    --foliage: #3d4a36;
    --person-light: #8a7a6a;
    --person-dark: #2d3440;
    --tag-purple: #8e2e94;
    --band-dark: rgba(28, 28, 30, 0.9);
    --ink-light: #ffffff;
  }
  html, body {
    margin: 0;
    padding: 0;
    overflow: hidden;
    background: #ffffff;
  }
  .banner {
    position: relative;
    width: 1200px;
    height: 202px;
    overflow: hidden;
  }
  .banner__scene {
    position: absolute;
    inset: 0;
    background:
      linear-gradient(90deg, var(--foliage) 0%, rgba(61,74,54,0.55) 18%, rgba(61,74,54,0) 34%),
      linear-gradient(180deg, var(--sky-top) 0%, var(--sky-mid) 48%, var(--sea) 66%, var(--sand) 100%);
  }
  .banner__portrait {
    position: absolute;
    left: 60px;
    top: 20px;
    width: 200px;
    height: 182px;
    border-radius: 90px 90px 0 0;
    background: linear-gradient(180deg, var(--person-light) 0%, var(--person-light) 45%, var(--person-dark) 70%, var(--person-dark) 100%);
    opacity: 0.9;
  }
  .banner__owner-tag {
    position: absolute;
    left: 272px;
    top: 19px;
    width: 214px;
    height: 44px;
  }
  .banner__owner-tag svg {
    position: absolute;
    inset: 0;
  }
  .banner__owner-name {
    position: absolute;
    left: 16px;
    top: 4px;
    margin: 0;
    font-family: "Philosopher", sans-serif;
    font-weight: 400;
    font-size: 30px;
    line-height: 36px;
    color: var(--ink-light);
    white-space: nowrap;
  }
  .banner__title-band {
    position: absolute;
    left: 310px;
    top: 63px;
    width: 690px;
    height: 84px;
  }
  .banner__title-band svg {
    position: absolute;
    inset: 0;
  }
  .banner__title {
    position: absolute;
    left: 42px;
    top: 2px;
    margin: 0;
    font-family: "Philosopher", sans-serif;
    font-weight: 400;
    font-size: 62px;
    line-height: 78px;
    color: var(--ink-light);
    white-space: nowrap;
  }
  .banner__tagline-band {
    position: absolute;
    left: 417px;
    top: 170px;
    width: 783px;
    height: 32px;
    background: var(--band-dark);
  }
  .banner__tagline {
    margin: 0;
    padding-left: 14px;
    font-family: "Noto Serif", serif;
    font-weight: 700;
    font-size: 18.5px;
    line-height: 32px;
    color: var(--ink-light);
    white-space: nowrap;
  }
</style>
</head>
<body>
  <header class="banner">
    <div class="banner__scene" role="img" aria-label="Photo of a palm-lined beach at sunset with calm sea and pale sky"></div>
    <div class="banner__portrait" role="img" aria-label="Photo of the blog's author smiling on the beach"></div>

    <div class="banner__owner-tag">
      <svg width="214" height="44" viewBox="0 0 214 44" aria-hidden="true">
        <polygon points="8,0 214,0 214,44 0,44" fill="var(--tag-purple)"/>
      </svg>
      <p class="banner__owner-name">Owen Pelsworth's</p>
    </div>

    <div class="banner__title-band">
      <svg width="690" height="84" viewBox="0 0 690 84" aria-hidden="true">
        <polygon points="14,0 690,0 676,84 0,84" fill="var(--band-dark)"/>
      </svg>
      <h1 class="banner__title">Harbour Lantern Guides</h1>
    </div>

    <div class="banner__tagline-band">
      <p class="banner__tagline">Luxurious destinations, transportation, accommodation and journeys.</p>
    </div>
  </header>
</body>
</html>
```